Tide Harbor Finance Business Cards

Looking for a business card for a new mortgage broking business. Name of the business is Tide Harbor Finance. Purpose of the business is to build trust and strong relationships with clients to then assist them with your mortgage lending needs. Most relationships within the business start off as an enquiry, and then can evolve into a 10+ year relationship, servicing clients from purchasing a new home to then upgrading for their family and even then assisting their children with their first home purchase. Business card should communicate financial security and trust.

Target Market(s)

Targeting professional clients who are looking to build a relationship with a knowledgeable mortgage professional

Industry/Entity Type

Finance - Home Loans

Contact Information for Business Card

Peter Colburn, Director, mobile: 0427 903186, email:peter@tideharborfinance.com.au, website: www.tideharborfinance.com.au

Font styles to use
Sans Serif

Requirements
Must have
• On the front: Must have company logo, contact details as above. On the back: slogan, 'full of choices, free of stress', plus listing services offered: home loans, investment loans, first home buyers, refinancing, car finance

```html
<!DOCTYPE html>
<html lang="en">
<head>
<meta charset="UTF-8">
<title>Tide Harbor Finance Business Cards</title>
<link href="https://fonts.googleapis.com/css2?family=Roboto:wght@400;700;900&display=swap" rel="stylesheet">
<style>
  :root {
    --navy: #0d4f7c;
    --navy-deep: #0a4470;
    --gold: #f0a431;
    --paper: #ffffff;
    --ink: #2b2b2b;
    --backdrop: #e9ebee;
  }
  * { margin: 0; padding: 0; box-sizing: border-box; }
  html, body { width: 1200px; height: 900px; overflow: hidden; }
  body {
    background: var(--backdrop);
    font-family: "Roboto", Arial, sans-serif;
    display: flex;
    flex-direction: column;
    align-items: center;
    justify-content: center;
    gap: 40px;
  }
  .card {
    position: relative;
    width: 660px;
    height: 377px;
    border-radius: 22px;
    overflow: hidden;
    box-shadow: 0 6px 18px rgba(0,0,0,0.18);
  }

  /* Back card */
  .card-back { background: var(--navy); color: var(--paper); }
  .card-back .brand {
    position: absolute; left: 150px; top: 62px;
    display: flex; align-items: center; gap: 16px;
  }
  .brand-mark {
    width: 22px; height: 22px; border-radius: 50%;
  }
  .card-back .brand-mark { background: var(--gold); }
  .brand-name {
    font-weight: 700; font-size: 34px; line-height: 1.05;
    text-transform: uppercase; letter-spacing: 0.5px;
  }
  .card-back .brand-name { color: var(--paper); }
  .slogan {
    position: absolute; left: 0; right: 0; top: 176px;
    text-align: center; font-weight: 900; font-size: 30px;
  }
  .services-title {
    position: absolute; left: 0; right: 0; top: 234px;
    text-align: center; font-weight: 900; font-size: 22px;
    letter-spacing: 4px; color: var(--gold); text-transform: uppercase;
  }
  .services-list {
    position: absolute; left: 0; right: 0; top: 272px;
    text-align: center; font-size: 18px; line-height: 1.5; list-style: none;
  }
  .services-list li { display: inline; }
  .services-list li::before { content: "\2022\00a0"; }
  .services-list li + li { margin-left: 10px; }

  /* Front card */
  .card-front { background: var(--paper); color: var(--ink); }
  .card-front .brand {
    position: absolute; right: 48px; top: 54px;
    display: flex; align-items: center; gap: 16px;
  }
  .card-front .brand-mark { background: var(--navy); }
  .card-front .brand-name { color: var(--navy); text-align: left; }
  .rule { position: absolute; height: 1px; background: #333; }
  .rule-top { left: 330px; right: 48px; top: 160px; }
  .rule-mid { left: 48px; right: 330px; top: 226px; }
  .person { position: absolute; left: 48px; top: 160px; }
  .person-name { font-weight: 900; font-size: 30px; color: var(--navy); }
  .person-role { font-size: 18px; margin-top: 2px; }
  .contact {
    position: absolute; display: flex; align-items: center; gap: 10px;
    font-size: 18px;
  }
  .contact svg { width: 18px; height: 18px; fill: var(--gold); }
  .contact-phone { left: 48px; top: 242px; }
  .contact-email { left: 350px; top: 176px; }
  .bands { position: absolute; left: 0; bottom: 0; width: 660px; height: 110px; }
  .website {
    position: absolute; right: 28px; bottom: 26px;
    font-size: 16px; color: var(--paper);
  }
</style>
</head>
<body>

  <section class="card card-back">
    <div class="brand">
      <span class="brand-mark"></span>
      <span class="brand-name">Tide Harbor<br>Finance</span>
    </div>
    <p class="slogan">Full of choices, free of stress</p>
    <p class="services-title">Listing services offered</p>
    <ul class="services-list">
      <li>Home loans</li><li>Investment loans</li><li>First home buyers</li><br>
      <li>Refinancing</li><li>Car finance</li>
    </ul>
  </section>

  <section class="card card-front">
    <div class="brand">
      <span class="brand-mark"></span>
      <span class="brand-name">Tide Harbor<br>Finance</span>
    </div>
    <div class="rule rule-top"></div>
    <div class="contact contact-email">
      <svg viewBox="0 0 24 24" aria-hidden="true"><path d="M2 5h20v14H2z M2 5l10 8 10-8" fill="var(--gold)"/><path d="M2 5l10 8 10-8" fill="none" stroke="#fff" stroke-width="1.6"/></svg>
      <span>peter@tideharborfinance.com.au</span>
    </div>
    <div class="person">
      <div class="person-name">Peter Colburn</div>
      <div class="person-role">Director</div>
    </div>
    <div class="rule rule-mid"></div>
    <div class="contact contact-phone">
      <svg viewBox="0 0 24 24" aria-hidden="true"><path d="M6.6 10.8c1.4 2.8 3.8 5.1 6.6 6.6l2.2-2.2c.3-.3.7-.4 1-.2 1.1.4 2.3.6 3.6.6.6 0 1 .4 1 1V20c0 .6-.4 1-1 1C10.6 21 3 13.4 3 4c0-.6.4-1 1-1h3.5c.6 0 1 .4 1 1 0 1.3.2 2.5.6 3.6.1.3 0 .7-.2 1z"/></svg>
      <span>0427 903186</span>
    </div>
    <svg class="bands" viewBox="0 0 660 110" preserveAspectRatio="none" aria-hidden="true">
      <path d="M0 92 L400 40 Q412 38 408 50 L400 62 L0 106 Z" fill="var(--gold)"/>
      <path d="M0 104 L398 60 Q410 56 418 40 Q424 28 440 24 L660 0 L660 110 L0 110 Z" fill="var(--navy-deep)"/>
    </svg>
    <span class="website">www.tideharborfinance.com.au</span>
  </section>

</body>
</html>
```